Start-up Dog Daycare Needs a Retractable Banner Design for Career Fair

We are a dog daycare located in San Francisco, California, called TailNest Dog Daycare. Our small but dog-knowledgeable team gets to interact with and care for dogs on a daily basis where we supervise playgroups of various sizes. We will like a modern yet fun banner to attract potential new hires and interns. We will like the final design to communicate that we are seeking people who love dogs but who are also hard workers that can thrive in a team setting.

The product specs are as follows:
Document Trim Size - 33.13 X 86.18 inches (84.1 X 218.9cm) with 3312 X 8618 pixels.
Full Bleed Size - 33.38 X 86.43 inches (84.8 X 219.5cm) with 3338 X 8643 pixels.

Additionally, to get a better idea of our brand, attached will be our Company Brand Identity.
Furthermore, attached will be the text we will like included onto our banner.

Target Market(s)

Students at a University

Industry/Entity Type

Pet Care

Font styles to use
Sans Serif

Colors
33a6d7
fbee3e

Requirements
Must have
• Our company logo must be incorporated onto our banner.
• Please include the text in the following order:
• 1. "Dog lovers come talk to us"
• 2. "Internships and full-time positions available"
• Banner Size Specifications:
• Full Bleed Size
• 33.38" x 86.43"
• 84.8 x 219.5 cm
• 3338 x 8643 pixels
• Document Trim Size
• 33.13" x 86.18"
• 84.1 x 218.9 cm
• 3312 x 8618 pixels
• Finished artwork should extend to fill the full bleed area to avoid white edges around.
Nice to have
• - Colors Blue and Yellow
• - Image(s) of a dog(s) playing

```html
<!DOCTYPE html>
<html lang="en">
<head>
<meta charset="utf-8">
<title>TailNest Dog Daycare – Career Fair Banner</title>
<link rel="stylesheet" href="https://fonts.googleapis.com/css2?family=Baloo+2:wght@600;700;800&family=Montserrat:wght@600&display=swap">
<style>
  :root {
    --canvas: #000000;
    --sky: #86c9e6;
    --sun: #fbee44;
    --sun-deep: #d5c718;
    --brand-blue: #33a6d7;
    --ink: #1f1f1f;
    --white: #ffffff;
    --coat-dark: #1b1c1e;
    --coat-mid: #3a4148;
  }
  * { margin: 0; padding: 0; box-sizing: border-box; }
  html, body {
    width: 1200px; height: 1200px; overflow: hidden;
    background: var(--canvas);
  }
  .banner {
    position: absolute;
    left: 368px; top: 0;
    width: 464px; height: 1200px;
    background: var(--sky);
    overflow: hidden;
    font-family: "Baloo 2", "Trebuchet MS", sans-serif;
  }
  .banner__waves {
    position: absolute; left: 0; top: 0;
    width: 464px; height: 1200px;
  }
  .brand {
    position: absolute; left: 0; width: 100%;
    text-align: center;
  }
  .brand__name {
    top: 166px;
    font-size: 44px; font-weight: 800;
    color: var(--sun);
    line-height: 1;
  }
  .brand__tagline {
    top: 232px;
    font-family: "Montserrat", Arial, sans-serif;
    font-size: 11px; font-weight: 600;
    letter-spacing: 2px;
    color: var(--ink);
  }
  .headline {
    position: absolute; left: 0; top: 268px; width: 100%;
    text-align: center; color: var(--white);
    font-weight: 800; line-height: 1;
  }
  .headline__main { display: block; font-size: 54px; }
  .headline__sub { display: block; font-size: 36px; margin-top: 6px; }
  .dog-photo {
    position: absolute;
    left: 16px; top: 404px;
    width: 420px; height: 340px;
    border-radius: 46% 46% 10px 10px / 55% 55% 10px 10px;
    background: radial-gradient(ellipse at 55% 55%, var(--coat-mid) 0%, var(--coat-dark) 60%, rgba(27,28,30,0) 100%);
    opacity: 0.9;
  }
  .offer {
    position: absolute; left: 0; top: 880px; width: 100%;
    text-align: center; color: var(--brand-blue);
    font-weight: 800; line-height: 1;
  }
  .offer__line { display: block; }
  .offer__line--lead { font-size: 54px; height: 64px; }
  .offer__line--rest { font-size: 46px; height: 58px; }
</style>
</head>
<body>
  <main class="banner">
    <svg class="banner__waves" viewBox="0 0 580 1500" preserveAspectRatio="none" aria-hidden="true">
      <path fill="var(--sun-deep)" d="M230 1012 Q420 950 580 930 L580 1500 L230 1500 Z"/>
      <path fill="var(--sun)" d="M0 960 Q310 985 580 1105 L580 1500 L0 1500 Z"/>
    </svg>

    <div class="brand brand__name">TailNest</div>
    <div class="brand brand__tagline">DOG DAYCARE</div>

    <h1 class="headline">
      <span class="headline__main">Dog Lovers</span>
      <span class="headline__sub">come talk to us!</span>
    </h1>

    <div class="dog-photo" role="img" aria-label="Photo of a black and white border collie peeking over a ledge with its paws resting on the edge"></div>

    <h2 class="offer">
      <span class="offer__line offer__line--lead">Internships</span>
      <span class="offer__line offer__line--lead">&amp; Full-time</span>
      <span class="offer__line offer__line--rest">positions</span>
      <span class="offer__line offer__line--rest">available</span>
    </h2>
  </main>
</body>
</html>
```